Business card for massage therapy company called Brook Fern Wellness

Need business card for massage therapy company called Brook Fern Wellness. Would like my logo on the front and the back of the card I have 3 options of logos and you can play with what looks better.

Would like this information displayed on the back of the card:

Marcus Ellery
Licensed Massage Therapist
321-555-0147
brookfern-example.com
brookfern_rest_

```html
<!DOCTYPE html>
<html lang="en">
<head>
<meta charset="utf-8">
<title>Brook Fern Wellness – Business Card</title>
<link rel="stylesheet" href="https://fonts.googleapis.com/css2?family=Montserrat:wght@400;500;600&display=swap">
<style>
  :root {
    --backdrop: #e3e3e3;
    --card: #efefee;
    --sage: #666d55;
    --clay: #b88a6a;
    --ink: #2b2b2b;
    --rule: #8a8a8a;
  }
  * { margin: 0; padding: 0; box-sizing: border-box; }
  html, body {
    width: 1200px; height: 1124px; overflow: hidden;
    background: var(--backdrop);
    font-family: "Montserrat", sans-serif;
  }
  .card {
    position: absolute; left: 252px; width: 696px; height: 398px;
    background: var(--card); border-radius: 26px; overflow: hidden;
  }
  .card--front { top: 134px; }
  .card--back { top: 593px; }

  .brand { position: absolute; left: 0; width: 100%; text-align: center; color: var(--sage); }
  .brand__ring {
    position: absolute; left: 50%; border: 2px solid var(--sage); border-radius: 50%;
    transform: translateX(-50%);
  }
  .brand__name {
    position: absolute; left: 0; width: 100%; font-weight: 500;
    text-transform: uppercase; line-height: 1;
  }

  .card--front .brand__ring { top: 45px; width: 104px; height: 104px; }
  .card--front .brand__name--main { top: 158px; font-size: 32px; letter-spacing: 2px; }
  .card--front .brand__name--sub { top: 196px; font-size: 16px; letter-spacing: 7px; }

  .card--back .brand__ring { top: 93px; width: 132px; height: 132px; }
  .card--back .brand__name--main { top: 238px; font-size: 42px; letter-spacing: 3px; }
  .card--back .brand__name--sub { top: 288px; font-size: 21px; letter-spacing: 9px; }

  .person { position: absolute; right: 376px; top: 276px; text-align: right; }
  .person__name { font-size: 22px; font-weight: 600; color: var(--sage); letter-spacing: 0.5px; line-height: 1.1; }
  .person__role { font-size: 15.5px; color: var(--ink); margin-top: 6px; letter-spacing: 0.3px; }

  .divider { position: absolute; left: 347px; top: 255px; width: 1px; height: 93px; background: var(--rule); }

  .contacts { position: absolute; left: 368px; top: 250px; list-style: none; }
  .contacts__item {
    display: flex; align-items: center; height: 26px;
    font-size: 16px; color: var(--ink); letter-spacing: 0.2px;
  }
  .contacts__icon { width: 15px; height: 15px; margin-right: 8px; flex: none; }
  .contacts__dot { width: 13px; height: 13px; border-radius: 50%; background: var(--clay); margin-right: 8px; flex: none; }

  .band { position: absolute; left: 0; bottom: 0; width: 696px; height: 15px; }
</style>
</head>
<body>
  <section class="card card--front">
    <div class="brand">
      <div class="brand__ring"></div>
      <div class="brand__name brand__name--main">Brook Fern</div>
      <div class="brand__name brand__name--sub">Wellness</div>
    </div>

    <div class="person">
      <div class="person__name">MARCUS ELLERY</div>
      <div class="person__role">Licensed Massage Therapist</div>
    </div>

    <div class="divider"></div>

    <ul class="contacts">
      <li class="contacts__item">
        <svg class="contacts__icon" viewBox="0 0 24 24"><path fill="var(--clay)" d="M6.6 10.8a15 15 0 0 0 6.6 6.6l2.2-2.2a1 1 0 0 1 1-.25 11.4 11.4 0 0 0 3.6.57 1 1 0 0 1 1 1V20a1 1 0 0 1-1 1A17 17 0 0 1 3 4a1 1 0 0 1 1-1h3.5a1 1 0 0 1 1 1c0 1.25.2 2.45.57 3.57a1 1 0 0 1-.25 1z"/></svg>
        321-555-0147
      </li>
      <li class="contacts__item">
        <svg class="contacts__icon" viewBox="0 0 24 24"><rect x="2" y="5" width="20" height="14" rx="2" fill="var(--clay)"/><path d="M3 6l9 7 9-7" fill="none" stroke="var(--card)" stroke-width="1.8"/></svg>
        info@brookfern-example.com
      </li>
      <li class="contacts__item">
        <svg class="contacts__icon" viewBox="0 0 24 24" fill="none" stroke="var(--clay)" stroke-width="1.8"><circle cx="12" cy="12" r="9.5"/><ellipse cx="12" cy="12" rx="4.5" ry="9.5"/><path d="M2.5 12h19M4 7h16M4 17h16"/></svg>
        www.brookfern-example.com
      </li>
      <li class="contacts__item">
        <span class="contacts__dot"></span>
        @brookfern_rest_
      </li>
    </ul>

    <svg class="band" viewBox="0 0 696 15" preserveAspectRatio="none">
      <polygon points="0,0 352,0 332,15 0,15" fill="var(--sage)"/>
      <polygon points="363,0 696,0 696,15 343,15" fill="var(--clay)"/>
    </svg>
  </section>

  <section class="card card--back">
    <div class="brand">
      <div class="brand__ring"></div>
      <div class="brand__name brand__name--main">Brook Fern</div>
      <div class="brand__name brand__name--sub">Wellness</div>
    </div>
  </section>
</body>
</html>
```